Business Card Design - Law Firm

I need a business card design. I have attached a picture of the law firm's website and logo. The business card design should be consistent with those pictures. There should be a place for the employee name, employee job title, telephone number, facsimile number, address, website url, and email address for each employee.
Industry/Entity Type
Business

```html
<!DOCTYPE html>
<html lang="en">
<head>
<meta charset="utf-8">
<title>Whitcombe Law – Business Card</title>
<link rel="stylesheet" href="https://fonts.googleapis.com/css2?family=Open+Sans:wght@400;600;700&display=swap">
<style>
  :root {
    --backdrop: #a07d24;
    --card-white: #ffffff;
    --ink: #2b2b2b;
    --ink-soft: #555555;
    --gold: #c9ad66;
    --gold-dark: #9b8240;
    --gold-light: #e3cf8e;
    --black: #1a1a1a;
    --silver-light: #f4f4f4;
    --silver-dark: #6d6d6d;
  }
  * { margin: 0; padding: 0; box-sizing: border-box; }
  html, body { width: 1200px; height: 686px; overflow: hidden; }
  body {
    background: var(--backdrop);
    font-family: "Open Sans", Arial, sans-serif;
    position: relative;
  }
  .card {
    position: absolute;
    width: 525px;
    height: 300px;
    overflow: hidden;
  }
  .card-front { left: 63px; top: 128px; background: var(--card-white); }
  .card-back {
    left: 611px; top: 297px;
    background: radial-gradient(ellipse at 52% 45%, var(--silver-light) 0%, #cfcfcf 45%, var(--silver-dark) 100%);
  }
  .accent-top-bar {
    position: absolute; left: 180px; top: 0; width: 320px; height: 10px;
    background: linear-gradient(90deg, var(--gold-dark), var(--gold-light) 55%, var(--gold-dark));
  }
  .accent-top-block {
    position: absolute; left: 461px; top: 10px; width: 64px; height: 12px;
    background: var(--black);
  }
  .accent-side-bar {
    position: absolute; left: 0; top: 215px; width: 10px; height: 67px;
    background: linear-gradient(180deg, var(--gold-light), var(--gold-dark));
    z-index: 1;
  }
  .accent-side-block {
    position: absolute; left: 0; top: 239px; width: 21px; height: 61px;
    background: var(--black);
  }
  .firm-name {
    position: absolute; left: 54px; top: 72px;
    font-size: 28px; font-weight: 400; color: var(--gold-dark);
    letter-spacing: 0.5px;
  }
  .contact {
    position: absolute; right: 56px; top: 104px;
    text-align: right; color: var(--ink);
  }
  .contact-name { font-size: 14px; font-weight: 700; color: var(--gold); line-height: 19px; }
  .contact-title { font-size: 13px; font-weight: 700; color: var(--ink-soft); line-height: 19px; }
  .contact-address { font-size: 12.5px; line-height: 18px; margin-top: 9px; }
  .contact-lines { list-style: none; margin-top: 11px; font-size: 12.5px; line-height: 19px; }
  .contact-lines li { display: flex; justify-content: flex-end; align-items: center; gap: 5px; }
  .contact-lines svg { width: 11px; height: 11px; fill: none; stroke: var(--gold); stroke-width: 1.6; }
  .back-name {
    position: absolute; left: 0; right: 0; top: 112px;
    text-align: center; font-size: 34px; font-weight: 400; color: var(--gold-dark);
  }
</style>
</head>
<body>
  <section class="card card-front" aria-label="Card front">
    <div class="accent-top-bar"></div>
    <div class="accent-top-block"></div>
    <div class="accent-side-bar"></div>
    <div class="accent-side-block"></div>

    <div class="firm-name">Whitcombe Law</div>

    <div class="contact">
      <p class="contact-name">Name</p>
      <p class="contact-title">Title</p>
      <p class="contact-address">48 Larkmoor Road, Suite 310<br>Danbury Hills, Vermont 4518</p>
      <ul class="contact-lines">
        <li>123-456-7890
          <svg viewBox="0 0 12 12"><path d="M2.5 1.5l2 2-1 1.5c.8 1.6 1.9 2.7 3.5 3.5l1.5-1 2 2-1.5 1.5C5 10.5 1.5 7 1 3z"/></svg>
        </li>
        <li>123-456-7890
          <svg viewBox="0 0 12 12"><rect x="1" y="5" width="10" height="5"/><rect x="3" y="1.5" width="6" height="3.5"/></svg>
        </li>
        <li>name@website.com
          <svg viewBox="0 0 12 12"><circle cx="6" cy="6" r="2"/><path d="M8 6v1c0 2 3 2 3-1a5 5 0 1 0-2 4"/></svg>
        </li>
        <li>www.website.com
          <svg viewBox="0 0 12 12"><circle cx="6" cy="6" r="5"/><path d="M1 6h10M6 1c-2.5 3-2.5 7 0 10M6 1c2.5 3 2.5 7 0 10"/></svg>
        </li>
      </ul>
    </div>
  </section>

  <section class="card card-back" aria-label="Card back">
    <div class="back-name">Whitcombe Law</div>
  </section>
</body>
</html>
```